Business Card Design

I need a business card for my resume writing business. I have a logo that Im not keen on anymore so I would like the business card to use my photo instead of a logo. I am for mid career and trades resumes and prefer not to do executive resumes so don't need to aim for exectives. I would like it to be colourful. I like bright sky blue and maybe some pink or purple but primarily bright sky blue. I don't like green and Im keen see a fair bit of white on the card. As I have a photo to go it, it will need to go on a white background.

Target Market(s)

mid range careers. Not executives

Industry/Entity Type

Business

Contact Information for Business Card

Wyn Marchetti
Resume Writer
Clear Path CVs
27 The Lanyard
HARWOOD NSW 2465
wyn@clearpathcvs.com.au
0417362958
www.clearpathcvs.com.au

Requirements
Nice to have
• Maybe colours similar to my website - www.clearpathcvs.com.au but not with any black on it.
Should not have
• No green or dark colours

```html
<!DOCTYPE html>
<html lang="en">
<head>
<meta charset="utf-8">
<title>Clear Path CVs – Business Card</title>
<link rel="stylesheet" href="https://fonts.googleapis.com/css2?family=Titillium+Web:wght@300;400;700&display=swap">
<style>
  :root {
    --sky-deep: #1a72bb;
    --sky-bright: #2aaee4;
    --pink: #ec1c7a;
    --magenta: #d91a5e;
    --plum: #9c1f62;
    --ink: #3a3a3c;
    --grey: #6d6e71;
    --edge: #9a9a9a;
    --white: #ffffff;
    --icon-ring: #8fd0f0;
  }
  * { margin: 0; padding: 0; box-sizing: border-box; }
  html, body {
    width: 1200px; height: 734px; overflow: hidden;
    background: var(--white);
    font-family: "Titillium Web", Arial, sans-serif;
  }
  .card {
    position: absolute; left: 16px; top: 2px;
    width: 1183px; height: 730px;
    border: 2px solid var(--edge);
    border-radius: 110px 0 28px 0;
    overflow: hidden;
    background: var(--white);
  }
  .portrait {
    position: absolute; left: 0; top: 0;
    width: 1183px; height: 730px;
  }
  .brand {
    position: absolute; left: 356px; top: 129px;
    display: flex; align-items: center; gap: 20px;
  }
  .brand-dash { width: 103px; height: 12px; background: var(--pink); }
  .brand-name {
    font-weight: 700; font-size: 35px; letter-spacing: 1.5px;
    color: var(--ink); line-height: 36px;
  }
  .address {
    position: absolute; left: 352px; top: 177px;
    font-size: 32px; font-weight: 400; color: var(--grey);
    letter-spacing: 0.3px; line-height: 38px;
  }
  .name-band {
    position: absolute; left: 0; top: 256px;
    width: 886px; height: 148px;
    background: linear-gradient(90deg, var(--sky-deep), var(--sky-bright));
  }
  .role {
    position: absolute; left: 74px; top: 66px;
    font-size: 24px; font-weight: 400; letter-spacing: 4.5px;
    color: var(--white); line-height: 30px;
  }
  .person {
    position: absolute; left: 372px; top: 46px;
    font-size: 56px; font-weight: 300; letter-spacing: 3px;
    color: var(--white); line-height: 66px; white-space: nowrap;
  }
  .contacts { position: absolute; left: 62px; top: 434px; list-style: none; }
  .contact { display: flex; align-items: center; height: 72px; }
  .contact svg { width: 58px; height: 58px; flex: none; }
  .contact span {
    margin-left: 17px; font-size: 32px; color: var(--grey);
    letter-spacing: 0.2px; line-height: 38px;
  }
  .stripe { position: absolute; top: 696px; height: 34px; }
  .stripe-plum { left: 0; width: 403px; background: var(--plum); }
  .stripe-magenta { left: 403px; width: 418px; background: var(--magenta); }
  .stripe-pink { left: 821px; width: 307px; background: var(--pink); border-radius: 0 30px 0 0; }
</style>
</head>
<body>
<div class="card">
  <svg class="portrait" viewBox="0 0 1183 730" role="img" aria-label="Portrait photograph of the resume writer">
    <defs>
      <linearGradient id="portrait-tone" x1="0" y1="0" x2="0" y2="1">
        <stop offset="0" stop-color="#1f3a4a"/>
        <stop offset="0.45" stop-color="#5f7f91"/>
        <stop offset="0.7" stop-color="#c9d8e1"/>
        <stop offset="1" stop-color="#eef3f6"/>
      </linearGradient>
    </defs>
    <path d="M1030 72 C 1120 72 1170 140 1183 220 L 1183 696 L 640 696 C 660 600 700 480 760 430 C 800 400 850 390 886 380 L 886 200 C 900 120 960 72 1030 72 Z" fill="url(#portrait-tone)"/>
  </svg>

  <div class="brand">
    <div class="brand-dash"></div>
    <div class="brand-name">CLEAR PATH CVS</div>
  </div>
  <div class="address">27 Lanyard HARWOOD NSW, 2465</div>

  <div class="name-band">
    <div class="role">RESUME WRITER</div>
    <div class="person">WYN MARCHETTI</div>
  </div>

  <ul class="contacts">
    <li class="contact">
      <svg viewBox="0 0 58 58" aria-hidden="true">
        <circle cx="29" cy="29" r="27" fill="var(--icon-ring)"/>
        <circle cx="29" cy="29" r="22" fill="var(--sky-bright)"/>
        <path d="M21 18c2-1 3 0 4 2l2 4c.6 1.4 0 2.3-1 3 1 2.5 3 4.6 5.5 5.6 .7-1 1.6-1.6 3-1l4 2c2 1 3 2 2 4-1.5 3-4 4-7 3-6-2-11-7-13-13-1-3 0-6.5 .5-7.6z" fill="var(--white)"/>
      </svg>
      <span>0417 362 958</span>
    </li>
    <li class="contact">
      <svg viewBox="0 0 58 58" aria-hidden="true">
        <circle cx="29" cy="29" r="27" fill="var(--icon-ring)"/>
        <circle cx="29" cy="29" r="22" fill="var(--sky-bright)"/>
        <rect x="16" y="20" width="26" height="18" fill="none" stroke="var(--white)" stroke-width="2.5"/>
        <path d="M16 20l13 11 13-11M16 38l10-9M42 38l-10-9" fill="none" stroke="var(--white)" stroke-width="2.2"/>
      </svg>
      <span>wyn@clearpathcvs.com.au</span>
    </li>
    <li class="contact">
      <svg viewBox="0 0 58 58" aria-hidden="true">
        <circle cx="29" cy="29" r="27" fill="var(--icon-ring)"/>
        <circle cx="29" cy="29" r="22" fill="var(--sky-bright)"/>
        <path d="M23 17v22l5-5 4 8 3-1.5-4-8h7z" fill="var(--sky-bright)" stroke="var(--white)" stroke-width="2.2" stroke-linejoin="round"/>
      </svg>
      <span>www.clearpathcvs.com.au</span>
    </li>
  </ul>

  <div class="stripe stripe-plum"></div>
  <div class="stripe stripe-magenta"></div>
  <div class="stripe stripe-pink"></div>
</div>
</body>
</html>
```